Talon Microchips PowerPoint Master Slide Deck Design

This is a 2-phase project to design a slide deck for a semiconductor company in the Silicon Valley. The design budget will be increased with each phase.
The slide deck will need to have one version with a dark background for presentations and a second version with a white background. Otherwise, the slides will be the same. I anticipate we will need a total of 10 slides, but that number may change.
The first phase will be to design a Title and a Title and Content slide.
- The Title Slide is the first slide of the deck. It should include the presentation title, the presenter's name and date of presentation
- The Title and Content slide should include a title and content with bullet points and up to 2 additional sub-bullets
- The Title and Content slide should have a footer that includes the slide #, Talon Microchips Confidential, and the logo. This footer will be on every slide except the Title Slide
The first two slides will serve as the format for the remaining ~8 slides:
-Header and Content Text (1, 2, 4 column)
-Header and Content Image (bar chart, pie chart, tables)
-Break
-Title only
-Closing (Talon logo only)
Our slides contain a lot of content so a clean and simple design is best.
Both phases will need to include pre-set color options for
-Text and Lines
-Shadows
-Bullets and sub-bullets (including shapes, ex. circle, slash, square, etc.)
-Bar charts, pie charts, tables
Samples of our collateral are attached. Logo files are also attached

```html
<!DOCTYPE html>
<html lang="en">
<head>
<meta charset="utf-8">
<title>Talon Microchips – Master Slide Deck</title>
<link href="https://fonts.googleapis.com/css2?family=Montserrat:wght@400;500;600;700&display=swap" rel="stylesheet">
<style>
:root{
  --page:#ffffff;
  --slide:#000000;
  --ink:#ffffff;
  --ink-soft:#d8dde6;
  --navy-deep:#050b14;
  --navy-mid:#0d2238;
  --teal:#1a4a66;
  --blue:#1e6fe8;
  --photo-dark:#071626;
  --photo-mid:#1d4f6e;
  --photo-glow:#3a86b0;
}
*{margin:0;padding:0;box-sizing:border-box}
html,body{width:1200px;height:4155px;overflow:hidden;background:var(--page)}
body{position:relative;font-family:"Montserrat",Arial,sans-serif;color:var(--ink)}
.slide{position:absolute;left:54px;width:1088px;height:613px;background:var(--slide);overflow:hidden}
.abs{position:absolute}
.brand{position:absolute;color:var(--ink);font-weight:600;line-height:1}
.brand .name{display:block;letter-spacing:.04em}
.brand .sub{display:block;letter-spacing:.06em}
.brand-lg .name{font-size:46px}
.brand-lg .sub{font-size:19px;margin-top:4px;padding-left:16px}
.brand-md .name{font-size:30px}
.brand-md .sub{font-size:12px;margin-top:2px;padding-left:10px}
.brand-xl .name{font-size:50px}
.brand-xl .sub{font-size:20px;margin-top:4px;padding-left:16px}
.brand-foot{display:flex;align-items:center;gap:6px}
.brand-foot .dot{width:14px;height:14px;border-radius:50%;background:var(--ink)}
.brand-foot .name{font-size:16px}
.brand-foot .sub{font-size:7px;margin-top:1px}
.footer-note{position:absolute;font-size:11px;font-weight:500;color:var(--ink);white-space:nowrap}
.heading{position:absolute;font-weight:600;font-size:22px;padding-bottom:6px;border-bottom:1.5px solid var(--ink);white-space:nowrap}
.heading-center{left:50%;transform:translateX(-50%)}
.body-copy{position:absolute;color:var(--ink-soft)}
.body-copy-side{font-size:8.8px;line-height:18px}
.body-copy-side p+p{margin-top:9px}
.body-copy-full{font-size:8.5px;line-height:20.4px}
.body-copy-full p+p{margin-top:40px}
/* slide 1 */
.title-main{position:absolute;left:10px;top:300px;font-size:36px;font-weight:600;white-space:nowrap}
.presenter{position:absolute;left:11px;top:350px;font-size:22px;font-weight:400}
/* slide 2 */
.circuit-bg{position:absolute;inset:0;background:radial-gradient(ellipse at 50% 70%,var(--teal) 0%,var(--navy-mid) 40%,var(--navy-deep) 85%)}
.col{position:absolute;top:216px;width:272px}
.col h3{font-size:12.5px;font-weight:700;margin-bottom:6px}
.col .lead{font-size:13.5px;line-height:20px;font-weight:500;margin-bottom:14px}
.col ul{list-style:none}
.col li{position:relative;padding-left:9px;font-size:9.5px;line-height:16px;color:var(--ink-soft);margin-bottom:15px}
.col li::before{content:"";position:absolute;left:0;top:6px;width:4px;height:4px;border-radius:50%;background:var(--ink)}
.col-accent{position:absolute;left:381px;top:517px;width:320px;height:4px;background:var(--blue)}
</style>
</head>
<body>

<!-- Slide 1 : Title -->
<section class="slide" style="top:59px">
  <div class="brand brand-lg" style="left:10px;top:200px"><span class="name">TALON</span><span class="sub">Microchips</span></div>
  <h1 class="title-main">Lorem ipsum dolor sit</h1>
  <p class="presenter">Marcus Lenhart</p>
</section>

<!-- Slide 2 : Title and Content (3 columns) -->
<section class="slide" style="top:734px">
  <div class="circuit-bg" role="img" aria-label="Dark blue close-up photograph of a printed circuit board"></div>
  <div class="brand brand-md" style="left:0;right:0;top:26px;text-align:center"><span class="name">TALON</span><span class="sub" style="padding-left:0">Microchips</span></div>
  <h2 class="heading heading-center" style="top:112px">Lorem ipsum dolor sit amet</h2>

  <div class="col" style="left:74px">
    <h3>Lorem ipsum</h3>
    <p class="lead">Lorem ipsum dolor sit met, consectetur adipscing elit, lacus vel facilisis.</p>
    <ul>
      <li>Lorem ipsum dolor sit met, consectetur adipscing elit, lacus vel facilisis.Lorem ipsum dolor sit met, consectetur adipscing elit, lacus vel facilisis.Lorem ipsum dolor sit met, consectetur adipscing.</li>
      <li>Lorem ipsum dolor sit met, consectetur adipscing elit, lacus vel facilisis.Lorem ipsum dolor sit met, consectetur adipscing elit, lacus vel facilisis.Lorem ipsum dolor sit met, consectetur adipscing.</li>
      <li>Lorem ipsum dolor sit met, consectetur adipscing elit, lacus vel facilisis.Lorem ipsum dolor sit met, consectetur adipscing elit, lacus vel facilisis.Lorem ipsum dolor sit met, consectetur adipscing.</li>
    </ul>
  </div>
  <div class="col" style="left:411px">
    <h3>Lorem ipsum</h3>
    <p class="lead">Lorem ipsum dolor sit met, consectetur adipscing elit, lacus vel facilisis.</p>
    <ul>
      <li>Lorem ipsum dolor sit met, consectetur adipscing elit, lacus vel facilisis.Lorem ipsum dolor sit met, consectetur adipscing elit, lacus vel facilisis.Lorem ipsum dolor sit met, consectetur adipscing.</li>
      <li>Lorem ipsum dolor sit met, consectetur adipscing elit, lacus vel facilisis.Lorem ipsum dolor sit met, consectetur adipscing elit, lacus vel facilisis.Lorem ipsum dolor sit met, consectetur adipscing.</li>
      <li>Lorem ipsum dolor sit met, consectetur adipscing elit, lacus vel facilisis.Lorem ipsum dolor sit met, consectetur adipscing elit, lacus vel facilisis.Lorem ipsum dolor sit met, consectetur adipscing.</li>
    </ul>
  </div>
  <div class="col" style="left:750px">
    <h3>Lorem ipsum</h3>
    <p class="lead">Lorem ipsum dolor sit met, consectetur adipscing elit, lacus vel facilisis.</p>
    <ul>
      <li>Lorem ipsum dolor sit met, consectetur adipscing elit, lacus vel facilisis.Lorem ipsum dolor sit met, consectetur adipscing elit, lacus vel facilisis.Lorem ipsum dolor sit met, consectetur adipscing.</li>
      <li>Lorem ipsum dolor sit met, consectetur adipscing elit, lacus vel facilisis.Lorem ipsum dolor sit met, consectetur adipscing elit, lacus vel facilisis.Lorem ipsum dolor sit met, consectetur adipscing.</li>
      <li>Lorem ipsum dolor sit met, consectetur adipscing elit, lacus vel facilisis.Lorem ipsum dolor sit met, consectetur adipscing elit, lacus vel facilisis.Lorem ipsum dolor sit met, consectetur adipscing.</li>
    </ul>
  </div>
  <div class="col-accent"></div>
  <p class="footer-note" style="left:12px;top:578px">Talon Microchips Confidential</p>
  <div class="brand brand-foot" style="left:960px;top:568px"><span class="dot"></span><span><span class="name">TALON</span><span class="sub">Microchips</span></span></div>
</section>

<!-- Slide 3 : Image and Content -->
<section class="slide" style="top:1411px;left:48px;width:1094px">
  <svg class="abs" style="left:0;top:0" width="520" height="613" viewBox="0 0 520 613" role="img" aria-label="Photograph of an engineer in a clean-room suit inspecting a circuit board">
    <defs>
      <linearGradient id="labPhoto" x1="0" y1="0" x2="1" y2="1">
        <stop offset="0" stop-color="#1d4f6e"/>
        <stop offset=".55" stop-color="#071626"/>
        <stop offset="1" stop-color="#3a86b0"/>
      </linearGradient>
    </defs>
    <path d="M0 0 H376 Q640 306 320 613 H0 Z" fill="url(#labPhoto)"/>
  </svg>
  <div class="brand brand-md" style="left:553px;top:24px"><span class="name">TALON</span><span class="sub">Microchips</span></div>
  <h2 class="heading" style="left:550px;top:108px">Lorem ipsum dolor sit amet</h2>
  <div class="body-copy body-copy-side" style="left:550px;top:162px;width:504px">
    <p>Lorem ipsum dolor sit amet, consectetur adipiscing elit, sed do eiusmod tempor incididunt ut labore et dolore magna aliqua. Quis ipsum suspendisse ultrices gravida. Risus commodo viverra umsan lacus vel facilisis.Lorem ipsum dolor sit amet, consectetur adipiscing elit, sed do eiusmod tempor incididunt ut labore et dolore magna aliqua. Quis ipsum suspendisse ultrices gravida. Risus commodo viverra umsan lacus vel facilisis.</p>
    <p>Lorem ipsum dolor sit amet, consectetur adipiscing elit, sed do eiusmod tempor incididunt ut labore et dolore magna aliqua. Quis ipsum suspendisse ultrices gravida. Risus commodo viverra umsan lacus vel facilisis.Lorem ipsum dolor sit amet, consectetur adipiscing elit, sed do eiusmod tempor incididunt ut labore et dolore magna aliqua. Quis ipsum suspendisse ultrices gravida. Risus commodo viverra umsan lacus vel facilisis.</p>
    <p>Lorem ipsum dolor sit amet, consectetur adipiscing elit, sed do eiusmod tempor incididunt ut labore et dolore magna aliqua. Quis ipsum suspendisse ultrices gravida. Risus commodo viverra umsan lacus vel facilisis.Lorem ipsum dolor sit amet, consectetur adipiscing elit, sed do eiusmod tempor incididunt ut labore et dolore magna aliqua. Quis ipsum suspendisse ultrices gravida. Risus commodo viverra umsan lacus vel facilisis.</p>
    <p>Lorem ipsum dolor sit amet, consectetur adipiscing elit, sed do eiusmod tempor incididunt ut labore et dolore magna aliqua. Quis ipsum suspendisse ultrices gravida. Risus commodo viverra umsan lacus vel facilisis.Lorem ipsum dolor sit amet, consectetur adipiscing elit, sed do eiusmod tempor incididunt ut labore et dolore magna aliqua. Quis ipsum suspendisse ultrices gravida.</p>
  </div>
  <p class="footer-note" style="left:378px;top:585px">Talon Microchips Confidential</p>
  <div class="brand brand-foot" style="left:970px;top:576px"><span class="dot"></span><span><span class="name">TALON</span><span class="sub">Microchips</span></span></div>
</section>

<!-- Slide 4 : Header and Content (1 column) -->
<section class="slide" style="top:2091px">
  <div class="brand brand-md" style="left:14px;top:20px"><span class="name">TALON</span><span class="sub">Microchips</span></div>
  <h2 class="heading" style="right:12px;top:16px">Lorem ipsum dolor sit amet</h2>
  <div class="body-copy body-copy-full" style="left:13px;top:96px;width:1062px">
    <p>Lorem ipsum dolor sit amet, consectetur adipiscing elit, sed do eiusmod tempor incididunt ut labore et dolore magna aliqua. Quis ipsum suspendisse ultrices gravida. Risus commodo viverra umsan lacus vel facilisis rem ipsum dolor sit amet, consectetur adipiscing elit, sed do eiusmod tempor incididunt ut labore et dolore magna aliqua. Quis ipsum suspendisse ultrices gravida. Risus commodo viverra umsan lacus vel facilisis.Lorem sum dolor sit amet, consectetur adipiscing elit, sed do eiusmod tempor incididunt ut labore et dolore magna aliqua. Quis ipsum suspendisse ultrices gravida. Risus commodo viverra umsan lacus vel facilisis.Lorem ipsum olor sit amet, consectetur adipiscing elit, sed do eiusmod tempor incididunt ut labore et dolore magna aliqua. Quis ipsum suspendisse ultrices gravida. Risus commodo viverra umsan lacus vel facilisis.Lorem psum dolor sit et, consectetur adipiscing elit, sed do eiusmod tempor incididunt ut labore et dolore magna aliqua. Quis ipsum suspendisse ultrices gravida. Risus commodo viverra umsan lacus vel facilisis.</p>
    <p>Lorem ipsum dolor sit amet, consectetur adipiscing elit, sed do eiusmod tempor incididunt ut labore et dolore magna aliqua. Quis ipsum suspendisse ultrices gravida. Risus commodo viverra umsan lacus vel facilisis rem ipsum dolor sit amet, consectetur adipiscing elit, sed do eiusmod tempor incididunt ut labore et dolore magna aliqua. Quis ipsum suspendisse ultrices gravida. Risus commodo viverra umsan lacus vel facilisis.Lorem sum dolor sit amet, consectetur adipiscing elit, sed do eiusmod tempor incididunt ut labore et dolore magna aliqua. Quis ipsum suspendisse ultrices gravida. Risus commodo viverra umsan lacus vel facilisis.Lorem ipsum olor sit amet, consectetur adipiscing elit, sed do eiusmod tempor incididunt ut labore et dolore magna aliqua. Quis ipsum suspendisse ultrices gravida. Risus commodo viverra umsan lacus vel facilisis.Lorem psum dolor sit et, consectetur adipiscing elit, sed do eiusmod tempor incididunt ut labore et dolore magna aliqua. Quis ipsum suspendisse ultrices gravida. Risus commodo viverra umsan lacus vel facilisis.</p>
    <p>Lorem ipsum dolor sit amet, consectetur adipiscing elit, sed do eiusmod tempor incididunt ut labore et dolore magna aliqua. Quis ipsum suspendisse ultrices gravida. Risus commodo viverra umsan lacus vel facilisis rem ipsum dolor sit amet, consectetur adipiscing elit, sed do eiusmod tempor incididunt ut labore et dolore magna aliqua. Quis ipsum suspendisse ultrices gravida. Risus commodo viverra umsan lacus vel facilisis.Lorem sum dolor sit amet, consectetur adipiscing elit, sed do eiusmod tempor incididunt ut labore et dolore magna aliqua. Quis ipsum suspendisse ultrices gravida. Risus commodo viverra umsan lacus vel facilisis.Lorem ipsum olor sit amet, consectetur adipiscing elit, sed do eiusmod tempor incididunt ut labore et dolore magna aliqua. Quis ipsum suspendisse ultrices gravida. Risus commodo viverra umsan lacus vel facilisis.Lorem psum dolor sit et, consectetur adipiscing elit, sed do eiusmod tempor incididunt ut labore et dolore magna aliqua. Quis ipsum suspendisse ultrices gravida. Risus commodo viverra umsan lacus vel facilisis.</p>
  </div>
  <p class="footer-note" style="left:14px;top:580px">Talon Microchips Confidential</p>
  <div class="brand brand-foot" style="left:966px;top:572px"><span class="dot"></span><span><span class="name">TALON</span><span class="sub">Microchips</span></span></div>
</section>

<!-- Slide 5 : Break -->
<section class="slide" style="top:2771px">
  <svg class="abs" style="left:560px;top:0" width="528" height="613" viewBox="560 0 528 613" role="img" aria-label="Illustration of a glowing microchip with blue circuit traces radiating outward">
    <defs>
      <radialGradient id="chipGlow" cx=".62" cy=".5" r=".6">
        <stop offset="0" stop-color="#9fd4ff"/>
        <stop offset=".2" stop-color="#1e6fe8"/>
        <stop offset=".7" stop-color="#0b2f7a"/>
        <stop offset="1" stop-color="#061a45"/>
      </radialGradient>
    </defs>
    <path d="M690 0 H1088 V613 H690 Q480 306 690 0 Z" fill="url(#chipGlow)"/>
  </svg>
  <div class="brand brand-md" style="left:12px;top:18px"><span class="name">TALON</span><span class="sub">Microchips</span></div>
  <h2 class="heading" style="left:62px;top:282px;font-size:31px;padding-bottom:10px">Lorem ipsum dolor sit amet</h2>
  <p class="footer-note" style="left:10px;top:578px">Talon Microchips Confidential</p>
  <div class="brand brand-foot" style="left:542px;top:566px"><span class="dot"></span><span><span class="name">TALON</span><span class="sub">Microchips</span></span></div>
</section>

<!-- Slide 6 : Closing -->
<section class="slide" style="top:3451px">
  <div class="brand brand-xl" style="left:0;right:0;top:236px;text-align:center"><span class="name">TALON</span><span class="sub" style="padding-left:0">Microchips</span></div>
  <p class="abs" style="left:0;right:0;top:362px;text-align:center;font-size:32px;font-weight:600">Thank You Talon Microchips</p>
</section>

</body>
</html>
```